Succession & Estate Planning firm needs a double-sided one page client handout

We need a client hand-out that highlights the top 10 Reasons to get a Pension Plan. It will need the 10 reasons as headings, with a short description of each reason (attached Word doc). It should communicate that a Pension Plan is flexible and provides security. Our usual client is a business owner/medical professional/entrepreneur. Have a look at our website for more info about our business www.marvelko.ca Our logo colours are 83c242, 3b3839, d5d5d5 We like clean, modern, info-graphics, not too cluttered, not too loudWe would like the ability to update the text/content ourselves, in the future.

```html
<!DOCTYPE html>
<html lang="en">
<head>
<meta charset="utf-8">
<title>Marvelko – Top 10 Reasons Handout</title>
<link href="https://fonts.googleapis.com/css2?family=Montserrat:wght@400;700;800&family=Source+Sans+3:wght@400;600;700&display=swap" rel="stylesheet">
<style>
  :root{
    --bg:#cbcbcb;
    --paper:#f7f7f7;
    --green:#7cc142;
    --green-brush:#6fb536;
    --green-deep:#00a651;
    --ink:#3b3839;
    --text:#2e2c2d;
    --grey:#d5d5d5;
  }
  *{box-sizing:border-box;margin:0;padding:0}
  html,body{width:1200px;height:1200px;overflow:hidden;background:var(--bg)}
  body{position:relative;font-family:"Source Sans 3",sans-serif;color:var(--text)}
  .page{position:absolute;top:257px;width:532px;height:687px;background:var(--paper);
        box-shadow:0 2px 6px rgba(0,0,0,.28);overflow:hidden}
  .page--front{left:58px}
  .page--back{left:610px}

  /* front */
  .front-art{position:absolute;inset:0;width:532px;height:687px}
  .brand{position:absolute;top:38px;left:0;width:100%;text-align:center}
  .brand__name{font-family:"Montserrat",sans-serif;font-weight:800;font-size:26px;letter-spacing:1px;color:var(--ink)}
  .front-url{position:absolute;top:628px;left:0;width:100%;text-align:center;
             font-family:"Montserrat",sans-serif;font-weight:800;font-size:20px;color:var(--green)}

  /* back */
  .title-banner{position:absolute;left:86px;top:22px;width:372px;height:69px}
  .title-banner svg{position:absolute;inset:0}
  .title-banner h1{position:relative;padding-top:15px;text-align:center;color:#fff;
                   font-family:"Montserrat",sans-serif;font-weight:800;font-size:15.4px;line-height:20px}
  .reasons{position:absolute;left:39px;top:113px;width:476px;list-style:none}
  .reason{position:relative;margin-bottom:5.5px}
  .reason::before{content:"";position:absolute;left:-17px;top:4px;width:8px;height:8px;
                  background:var(--green);border-radius:0 80% 0 80%}
  .reason h2{font-size:12.4px;font-weight:700;color:var(--green);line-height:14px}
  .reason p{font-size:10px;line-height:12.8px}
  .back-footer{position:absolute;left:0;bottom:0;width:532px;height:62px}
  .back-footer svg{position:absolute;inset:0}
  .back-url{position:relative;padding-top:16px;text-align:center;color:#fff;
            font-family:"Montserrat",sans-serif;font-weight:800;font-size:19.5px}
</style>
</head>
<body>

<section class="page page--front">
  <svg class="front-art" viewBox="0 0 532 687">
    <defs>
      <linearGradient id="sunset" x1="0" y1="0" x2="0.3" y2="1">
        <stop offset="0" stop-color="#f6e6cf"/>
        <stop offset="0.45" stop-color="#e9b46a"/>
        <stop offset="0.75" stop-color="#a8782f"/>
        <stop offset="1" stop-color="#6b5224"/>
      </linearGradient>
    </defs>
    <g role="img" aria-label="Photo: family flying a kite in a sunlit field at sunset">
      <path d="M0,125 C160,175 360,205 532,175 L532,655 C380,590 210,545 0,560 Z" fill="url(#sunset)"/>
    </g>
    <path d="M0,70 C120,130 300,175 532,165 L532,168 C330,215 150,200 0,140 Z" fill="var(--green-deep)"/>
    <path d="M0,118 C150,165 330,185 532,168 L532,198 C350,235 170,220 0,155 Z" fill="var(--green)"/>
    <path d="M0,508 C180,500 360,560 532,650 L532,687 L0,687 Z" fill="var(--green-deep)"/>
    <path d="M0,530 C190,520 360,580 532,655 L532,687 L0,687 Z" fill="var(--green)"/>
    <path d="M0,580 C190,545 360,590 532,658 L532,687 L0,687 Z" fill="var(--paper)"/>
  </svg>
  <div class="brand">
    <span class="brand__name">Marvelko</span>
  </div>
  <div class="front-url">www.marvelko.ca</div>
</section>

<section class="page page--back">
  <div class="title-banner">
    <svg viewBox="0 0 372 69" preserveAspectRatio="none">
      <path d="M20,4 L300,2 L312,8 L338,12 L320,18 L350,24 L334,30 L368,44 L340,48 L360,56 L320,62 L300,68 L60,67 L20,64 L2,58 L16,50 L4,44 L12,32 L0,26 L8,20 L2,14 L26,10 Z" fill="var(--green-brush)"/>
    </svg>
    <h1>Top 10 Reasons Why an FPP<br>Serves Your Family Enterprise</h1>
  </div>

  <ol class="reasons">
    <li class="reason"><h2>Create Significant Deductions</h2>
      <p>The FPP creates significant tax deductions, which can be used to keep the business under the small business rate or applied to the high rate, a bigger bang for the buck.</p></li>
    <li class="reason"><h2>Deliberate, Planned, Future Income</h2>
      <p>An income for beyond the last day at the office.</p></li>
    <li class="reason"><h2>Past Buy Back</h2>
      <p>Most owners invest, first, in the business. The FPP offers the ability to go back and recover lost years when they did not buy RRSPs…and pass the tax savings onto their company.</p></li>
    <li class="reason"><h2>Creditor Proof</h2>
      <p>All Assets held in an FPP are creditor proof, including RRSPs, and planned pension contributions receive “super-priority” status, which rank above the claims of secured creditors, like major commercial lenders and banks.</p></li>
    <li class="reason"><h2>Flexibility</h2>
      <p>Owners know that cash flows can swing wildly with the business cycle. An FPP offers the flexibility to flip between DB and DC accounts in order to conserve cash, smooth income during volatile years, and recover assets when things improve.</p></li>
    <li class="reason"><h2>Preserve the Lifetime Capital Gains Exemption</h2>
      <p>Create $1.6 Million++ of Tax Free Capital Gains. The significant deductions created in an FPP can be used to purify a corporation with passive assets, which can help preserve the shareholders’ lifetime capital gains exemption.</p></li>
    <li class="reason"><h2>Intergenerational Wealth Transfer</h2>
      <p>Unlike RRSPs that eventually trigger a taxable disposition upon death, an FPP has the ability to pass, tax deferred, to the next generation of family business owners.</p></li>
    <li class="reason"><h2>All Ages</h2>
      <p>An FPP can benefit all entrepreneurs between ages 18-71.</p></li>
    <li class="reason"><h2>Conserve the Small Business Deduction</h2>
      <p>Investment income inside an FPP grows tax exempt and does not create passive income as outlined under the 2018 “Passive Income Measures”. Therefore, business owners that redirect corporate resources to fund their pension assets will not jeopardize their low corporate tax rate on profits and in associated companies.</p></li>
    <li class="reason"><h2>Broader Investment Options</h2>
      <p>An FPP allows entrepreneurs to invest in what they like: real estate, other businesses and/or franchises, private equity, public equity, exempt markets, etc. The possibilities are up to the imagination of the entrepreneur and their advisors.</p></li>
  </ol>

  <footer class="back-footer">
    <svg viewBox="0 0 532 62" preserveAspectRatio="none">
      <path d="M0,6 L30,4 L60,7 L95,3 L130,6 L170,2 L210,6 L250,3 L290,7 L330,2 L370,6 L410,3 L450,6 L490,2 L532,5 L532,62 L0,62 Z" fill="var(--green-brush)"/>
    </svg>
    <div class="back-url">www.marvelko.ca</div>
  </footer>
</section>

</body>
</html>
```